Hollowbrook Yard Services - Needs a business card! Easy JOB!

I need a business card for a new company called Hollowbrook Yard Services. I will be offering the below services.

I am relatively open for ideas, so please be at your creative best.

I think I will list all the services offered on the rear of the card.

- Gardening
- Lawn Care
- Hedge Trimming
- Rubbish Removal
- Weeding/Spraying
- Landscaping
- Gutter Cleaning
- Solar Panel Cleaning
- Irrigation
- Pruning
- On-Site Mulching
- Ask for other services

I am still a little undecided on the colours. I prefer the logos with the Blue text, but I am open for ideas ( the logo/texts colours are not final).

Please use the catch phrase "What can Hollowbrook do for you?"

Here are the required details.

Hollowbrook Yard Services

Miles Fenwarick (owner)
Ph: 1300 555 014
Mob: 0400 555 286

miles@hollowbrookyard.com.au
www.hollowbrookyard.com.au
facebook.com/HollowbrookYard
twitter.com/HollowbrookYard
ABN: 555 019 472 ( this can be in smaller text somewhere, this is the least important )

Thankyou in advance! And good luck.

regards,
Miles
Updates

Hi everyone, please make sure you include the phrase "What can Hollowbrook do for you?" on the designs.

thanks,
Miles

Definitely liking the focus on a majority of the design on the blue colour from the logo. Also a splash of green in the plant.

Please make sure you list the services provided on the rear of the card. thanks.

With the service listing, please make "ask for other services" stand out, either a different colour or position or size... as long as it is more noticeable than the other services listed. Thanks.

Industry/Entity Type

Business

Requirements
Must have
• - use the font supplied (Brandon Family Font)
- use of the catch phrase "What can Hollowbrook do for you?"
- Double sided design
- Chatterly and Quipster logos/links
- Please use symbol/picture for "phone" "mobile" "email" instead of using the words.
- List the services provided on the rear of the card

```html
<!DOCTYPE html>
<html lang="en">
<head>
<meta charset="utf-8">
<title>Hollowbrook Yard Services – Business Card Options</title>
<link rel="stylesheet" href="https://fonts.googleapis.com/css2?family=Sorts+Mill+Goudy&family=Source+Sans+3:wght@400;600;700&display=swap">
<style>
  :root {
    --backdrop: #b88a27;
    --card-grey: #48494b;
    --brand-yellow: #f3ea00;
    --leaf-light: #a9d83d;
    --leaf-deep: #7cc042;
    --ink-dark: #3f4042;
    --head-green: #8dc63f;
    --white: #ffffff;
    --serif: "Sorts Mill Goudy", Georgia, serif;
    --sans: "Source Sans 3", "Helvetica Neue", Arial, sans-serif;
  }
  * { margin: 0; padding: 0; box-sizing: border-box; }
  html, body { width: 1200px; height: 686px; overflow: hidden; background: var(--backdrop); }
  .presentation { position: relative; width: 1200px; height: 686px; }

  .card {
    position: absolute; width: 450px; height: 256px;
    border-radius: 17px; overflow: hidden;
    background: var(--card-grey);
    box-shadow: 2px 3px 6px rgba(0,0,0,.45);
  }
  .card--front.row-1 { left: 147px; top: 54px; }
  .card--back.row-1  { left: 639px; top: 60px; height: 259px; }
  .card--front.row-2 { left: 147px; top: 369px; }
  .card--back.row-2  { left: 639px; top: 375px; height: 258px; }

  .card__waves { position: absolute; inset: 0; }

  /* Front: brand block */
  .brand-mark {
    position: absolute; left: 84px; top: 58px;
    width: 54px; height: 54px; border-radius: 50%;
    background: var(--leaf-light);
  }
  .brand-name {
    position: absolute; left: 8px; width: 200px; top: 182px;
    text-align: center; color: var(--leaf-light);
    font-family: var(--sans); font-weight: 700; text-transform: uppercase;
    line-height: 1;
  }
  .brand-name__main { display: block; font-size: 25px; letter-spacing: .3px; }
  .brand-name__sub { display: block; font-size: 12.5px; margin-top: 5px; letter-spacing: .3px; }

  /* Front: contact block */
  .contact {
    position: absolute; right: 8px; top: 0; width: 240px; height: 100%;
    color: var(--ink-dark); text-align: right;
  }
  .contact__name { position: absolute; right: 8px; top: 34px; font-size: 17.5px; white-space: nowrap; }
  .contact__role { position: absolute; right: 8px; top: 57px; font-size: 13px; }
  .contact__line {
    position: absolute; right: 0; font-size: 12.5px; white-space: nowrap;
    display: flex; align-items: center; gap: 4px;
  }
  .contact__line--small { font-size: 11px; }
  .contact__abn { position: absolute; right: 8px; top: 206px; font-size: 12.5px; }
  .icon { width: 11px; height: 11px; flex: none; }
  .icon--social { width: 11px; height: 11px; border-radius: 50%; background: var(--ink-dark); }

  .serif-set { font-family: var(--serif); }
  .serif-set .contact__name { letter-spacing: .2px; }
  .sans-set { font-family: var(--sans); }
  .sans-set .contact__name, .sans-set .contact__role { font-weight: 600; }
  .sans-set .contact__abn b { font-weight: 700; }

  /* Back */
  .back-mark {
    position: absolute; left: 132px; top: 48px;
    width: 52px; height: 52px; border-radius: 50%;
    background: var(--leaf-light);
  }
  .back-divider {
    position: absolute; left: 206px; top: 22px; width: 1px; height: 94px;
    background: #1f2021;
  }
  .back-name {
    position: absolute; left: 215px; top: 48px;
    font-family: var(--sans); font-weight: 700; font-size: 15px; line-height: 15px;
    color: var(--brand-yellow); text-transform: uppercase;
  }
  .back-tagline {
    position: absolute; left: 0; right: 0; top: 118px; text-align: center;
    color: var(--head-green); font-size: 17px;
  }
  .services {
    position: absolute; left: 0; right: 0; top: 143px;
    list-style: none; text-align: center;
    font-size: 13.4px; line-height: 20.6px; white-space: nowrap;
  }
  .services li span { margin: 0 5px; }
  .serif-set .services { color: var(--white); }
  .sans-set .back-tagline { font-weight: 700; }
  .sans-set .services { color: var(--brand-yellow); font-size: 13.4px; line-height: 19.6px; top: 146px; }
</style>
</head>
<body>
<main class="presentation">

  <!-- Option 1: serif set -->
  <section class="card card--front row-1 serif-set">
    <svg class="card__waves" viewBox="0 0 450 256" aria-hidden="true">
      <defs>
        <linearGradient id="leafFill1" x1="0" y1="0" x2="1" y2="1">
          <stop offset="0" stop-color="#a9d83d"/><stop offset="1" stop-color="#7cc042"/>
        </linearGradient>
      </defs>
      <path d="M191,0 C205,80 212,170 236,256 L450,256 L450,0 Z" fill="var(--brand-yellow)"/>
      <path d="M223,0 C230,80 236,170 250,256 L450,256 L450,0 Z" fill="var(--card-grey)"/>
      <path d="M232,0 C240,80 246,170 259,256 L450,256 L450,0 Z" fill="url(#leafFill1)"/>
    </svg>
    <div class="brand-mark"></div>
    <div class="brand-name"><span class="brand-name__main">Hollowbrook</span><span class="brand-name__sub">Yard Services</span></div>
    <div class="contact">
      <p class="contact__name">Miles Fenwarick</p>
      <p class="contact__role">Owner</p>
      <p class="contact__line" style="top:87px">1300 555 014
        <svg class="icon" viewBox="0 0 12 12"><path d="M2.5 1 L4.5 1 L5.2 3.5 L4 4.5 C4.7 6 6 7.3 7.5 8 L8.5 6.8 L11 7.5 L11 9.5 C11 10.4 10.3 11 9.5 11 C5 10.6 1.4 7 1 2.5 C1 1.7 1.6 1 2.5 1Z" fill="var(--ink-dark)"/></svg></p>
      <p class="contact__line" style="top:108px">0400 555 286
        <svg class="icon" viewBox="0 0 12 12"><rect x="3" y="0.5" width="6" height="11" rx="1" fill="var(--ink-dark)"/><rect x="4" y="2" width="4" height="6" fill="#cfe88f"/></svg></p>
      <p class="contact__line contact__line--small" style="top:126px">miles@hollowbrookyard.com.au
        <svg class="icon" viewBox="0 0 12 12"><rect x="0.5" y="2.5" width="11" height="7" fill="var(--ink-dark)"/><path d="M0.5 2.5 L6 6.5 L11.5 2.5" stroke="#cfe88f" stroke-width="0.8" fill="none"/></svg></p>
      <p class="contact__line contact__line--small" style="top:145px">www.hollowbrookyard.com.au
        <svg class="icon" viewBox="0 0 12 12"><circle cx="6" cy="6" r="5.3" fill="var(--ink-dark)"/><path d="M0.7 6 H11.3 M6 0.7 V11.3 M6 0.7 C3 3.5 3 8.5 6 11.3 M6 0.7 C9 3.5 9 8.5 6 11.3" stroke="#cfe88f" stroke-width="0.6" fill="none"/></svg></p>
      <p class="contact__line" style="top:164px">HollowbrookYard/ <span class="icon icon--social" aria-label="Chatterly"></span></p>
      <p class="contact__line" style="top:184px">HollowbrookYard/ <span class="icon icon--social" aria-label="Quipster"></span></p>
      <p class="contact__abn">ABN : 555 019 472</p>
    </div>
  </section>

  <section class="card card--back row-1 serif-set">
    <div class="back-mark"></div>
    <div class="back-divider"></div>
    <p class="back-name">Hollowbrook<br>Yard<br>Services</p>
    <p class="back-tagline">What can Hollowbrook do for you?</p>
    <ul class="services">
      <li><span>- Gardening</span><span>- Lawn Care</span><span>- Hedge Trimming</span></li>
      <li><span>- Rubbish Removal</span><span>- Weeding/Spraying</span><span>- Landscaping</span></li>
      <li><span>- Gutter Cleaning</span><span>- Solar Panel Cleaning</span><span>- Irrigation</span></li>
      <li><span>- Pruning</span><span>- On-Site Mulching</span><span>- Ask for other services</span></li>
    </ul>
  </section>

  <!-- Option 2: sans set -->
  <section class="card card--front row-2 sans-set">
    <svg class="card__waves" viewBox="0 0 450 256" aria-hidden="true">
      <defs>
        <linearGradient id="leafFill2" x1="0" y1="0" x2="1" y2="1">
          <stop offset="0" stop-color="#a9d83d"/><stop offset="1" stop-color="#7cc042"/>
        </linearGradient>
      </defs>
      <path d="M191,0 C205,80 212,170 236,256 L450,256 L450,0 Z" fill="var(--brand-yellow)"/>
      <path d="M223,0 C230,80 236,170 250,256 L450,256 L450,0 Z" fill="var(--card-grey)"/>
      <path d="M232,0 C240,80 246,170 259,256 L450,256 L450,0 Z" fill="url(#leafFill2)"/>
    </svg>
    <div class="brand-mark"></div>
    <div class="brand-name"><span class="brand-name__main">Hollowbrook</span><span class="brand-name__sub">Yard Services</span></div>
    <div class="contact">
      <p class="contact__name">Miles Fenwarick</p>
      <p class="contact__role">Owner</p>
      <p class="contact__line" style="top:89px">1300 555 014
        <svg class="icon" viewBox="0 0 12 12"><path d="M2.5 1 L4.5 1 L5.2 3.5 L4 4.5 C4.7 6 6 7.3 7.5 8 L8.5 6.8 L11 7.5 L11 9.5 C11 10.4 10.3 11 9.5 11 C5 10.6 1.4 7 1 2.5 C1 1.7 1.6 1 2.5 1Z" fill="var(--ink-dark)"/></svg></p>
      <p class="contact__line" style="top:109px">0400 555 286
        <svg class="icon" viewBox="0 0 12 12"><rect x="3" y="0.5" width="6" height="11" rx="1" fill="var(--ink-dark)"/><rect x="4" y="2" width="4" height="6" fill="#cfe88f"/></svg></p>
      <p class="contact__line contact__line--small" style="top:128px">miles@hollowbrookyard.com.au
        <svg class="icon" viewBox="0 0 12 12"><rect x="0.5" y="2.5" width="11" height="7" fill="var(--ink-dark)"/><path d="M0.5 2.5 L6 6.5 L11.5 2.5" stroke="#cfe88f" stroke-width="0.8" fill="none"/></svg></p>
      <p class="contact__line contact__line--small" style="top:146px">www.hollowbrookyard.com.au
        <svg class="icon" viewBox="0 0 12 12"><circle cx="6" cy="6" r="5.3" fill="var(--ink-dark)"/><path d="M0.7 6 H11.3 M6 0.7 V11.3 M6 0.7 C3 3.5 3 8.5 6 11.3 M6 0.7 C9 3.5 9 8.5 6 11.3" stroke="#cfe88f" stroke-width="0.6" fill="none"/></svg></p>
      <p class="contact__line" style="top:165px">HollowbrookYard/ <span class="icon icon--social" aria-label="Chatterly"></span></p>
      <p class="contact__line" style="top:185px">HollowbrookYard/ <span class="icon icon--social" aria-label="Quipster"></span></p>
      <p class="contact__abn"><b>ABN</b> : 555 019 472</p>
    </div>
  </section>

  <section class="card card--back row-2 sans-set">
    <div class="back-mark"></div>
    <div class="back-divider"></div>
    <p class="back-name">Hollowbrook<br>Yard<br>Services</p>
    <p class="back-tagline">What can Hollowbrook do for you?</p>
    <ul class="services">
      <li><span>- Gardening</span><span>- Lawn Care</span><span>- Hedge Trimming</span></li>
      <li><span>- Rubbish Removal</span><span>- Weeding/Spraying</span><span>- Landscaping</span></li>
      <li><span>- Gutter Cleaning</span><span>- Solar Panel Cleaning</span><span>- Irrigation</span></li>
      <li><span>- Pruning</span><span>- On-Site Mulching</span><span>- Ask for other services</span></li>
    </ul>
  </section>

</main>
</body>
</html>
```